Music Industry Business Needs a Business Card Design

Copper Lantern is an audio mastering company that has been in business for 20 years. Mastering is the final creative step in the music production chain. Our job is to make the music sound as good as it possibly can prior to release to the public. Our world is technical, artistic, precise. We work on everything from independent artists to the music for the Grandfield Cup. We are looking for a new, more modern business card design. I am uploading a copy of our logo, although it doesn't absolutely need to be included in the design.

Target Market(s)

Music Industry Professionals

Industry/Entity Type

Business

Contact Information for Business Card

Address, Phone, Email, Website, Name, Job Title

Font styles to use
Sans Serif

Requirements
Must have
• Sorry, but I don't have any concrete things to request. If I had a clear idea of what I want, I would probably just design something myself. I am looking for fresh input and thought I would try this.
Should not have
• Anything that is typical, such as headphones or the like.

```html
<!DOCTYPE html>
<html lang="en">
<head>
<meta charset="utf-8">
<title>Copper Lantern – Business Card</title>
<link rel="stylesheet" href="https://fonts.googleapis.com/css2?family=Oxygen:wght@300;400&display=swap">
<style>
  :root {
    --card-black: #0b0b0b;
    --card-deep: #161616;
    --glow-grey: #5a5a5a;
    --text-white: #f2f2f2;
    --rule-grey: #9a9a9a;
    --accent-amber: #f5a800;
    --band-light: #d9d9d9;
  }
  html, body {
    margin: 0;
    padding: 0;
    width: 1200px;
    height: 720px;
    overflow: hidden;
    background: var(--card-black);
  }
  .card {
    position: relative;
    width: 1200px;
    height: 720px;
    overflow: hidden;
    font-family: "Oxygen", "Segoe UI", sans-serif;
    font-weight: 300;
    color: var(--text-white);
    background:
      radial-gradient(ellipse 520px 300px at 0% 0%, rgba(90,90,90,0.55), transparent 70%),
      radial-gradient(ellipse 260px 380px at 100% 62%, rgba(110,110,110,0.55), transparent 75%),
      radial-gradient(ellipse 700px 420px at 55% 55%, var(--card-deep), var(--card-black) 80%);
  }
  .brand {
    position: absolute;
    left: 808px;
    top: 129px;
    display: flex;
    align-items: center;
    gap: 14px;
    color: var(--accent-amber);
    font-size: 41px;
    font-weight: 400;
    letter-spacing: 0.5px;
    text-transform: uppercase;
    white-space: nowrap;
  }
  .brand-dot {
    width: 14px;
    height: 14px;
    border-radius: 50%;
    background: var(--accent-amber);
  }
  .person-name {
    position: absolute;
    left: 131px;
    top: 206px;
    margin: 0;
    font-size: 57px;
    font-weight: 300;
    line-height: 1;
  }
  .name-rule {
    position: absolute;
    left: 135px;
    top: 274px;
    width: 806px;
    height: 1px;
    background: var(--rule-grey);
  }
  .job-title {
    position: absolute;
    left: 143px;
    top: 284px;
    margin: 0;
    font-size: 21px;
  }
  .contact {
    position: absolute;
    left: 460px;
    top: 358px;
    display: grid;
    grid-template-columns: 218px auto;
    column-gap: 23px;
    font-size: 27px;
    line-height: 33.5px;
  }
  .contact dt { text-align: right; }
  .contact dd { margin: 0; }
  .contact .address-label { margin-top: 29px; }
  .contact .address-lines { margin-top: 29px; }
  .music-motif {
    position: absolute;
    left: 0;
    top: 465px;
    width: 470px;
    height: 235px;
    background: radial-gradient(ellipse 230px 110px at 40% 55%, rgba(120,120,120,0.22), transparent 75%);
  }
  .footer-band {
    position: absolute;
    left: 0;
    bottom: 0;
    width: 1200px;
    height: 13px;
    background: var(--accent-amber);
    border-top: 2px solid var(--band-light);
  }
</style>
</head>
<body>
  <div class="card">
    <div class="brand"><span class="brand-dot"></span>Copper Lantern</div>

    <h1 class="person-name">Your Name</h1>
    <div class="name-rule"></div>
    <p class="job-title">General Manager</p>

    <dl class="contact">
      <dt>Mobile :</dt><dd>+001234567</dd>
      <dt>Email :</dt><dd>yourmail@email.com</dd>
      <dt>Website :</dt><dd>www.copperlantern.com</dd>
      <dt class="address-label">Address :</dt>
      <dd class="address-lines">“Copper Lantern”,<br>Your Street Rode,<br>Your Lane,<br>Your Country</dd>
    </dl>

    <div class="music-motif" role="img" aria-label="Faint musical staff with treble clef and flowing notes"></div>

    <div class="footer-band"></div>
  </div>
</body>
</html>
```